"Built on the grind" fitness and nutrition website/blog/forum

We need a website design for a gym training/nutrition website/blog. It is going to eventually have articles aimed at both men and women and will have content about exercise, nutrition, and the science behind both.

I want to have:
a home page
a page for all articles/blog posts about Nutrition
a page for all articles/blog posts about Training
a page where we can share articles about workouts targeting different muscle groups
a forum, where people can discuss nutrition and training (I would want this to be fairly simple to use and control as I am not a coder/programmer)

Design wise, I would like to use high contrast colours, such as black and white, but definitely open to some sort of colour theme, maybe some blue, or red, or purple, I am not sure, I would have to see an example.

We will be monetising this site with adverts, so there needs to be some space built in for this in the theme, however we don't want this to be overbearing, I don't want this to look like a spam site.

We have a logo, I have attached this. I haven't written any content for the homepage yet, as I wanted the design first before I worked out what to write and where to put it.

We will have social media accounts on instagram, twitter and facebook so would like buttons on the header and footer for these.

Target Market(s)

Fitness enthusiasts

Industry/Entity Type

fitness

Coding

Coded - Design and coding required

Number of Pages Required

5+ page

Font styles to use
Serif
Sans Serif

Colors

Designer to choose colors to be used in the design.

Requirements
Must have
• Space for some ads, a forum area, a page for nutrition blog posts, a page for training posts, a page for workout posts.

```html
<!DOCTYPE html>
<html lang="en">
<head>
<meta charset="utf-8">
<title>Built on the grind</title>
<link href="https://fonts.googleapis.com/css2?family=Kanit:ital,wght@1,800;1,900&family=Playfair+Display:ital,wght@1,800&family=Roboto:wght@400;500;700&display=swap" rel="stylesheet">
<style>
:root{
  --red:#e2151e;
  --red-dark:#b70d15;
  --ink:#1d1d1f;
  --dark:#2a2a2c;
  --grey:#efeff1;
  --line:#d9d9dd;
  --text:#555;
  --white:#fff;
  --fb:#3b5ba0;--tw:#34a3e0;--ig:#d2407c;--in:#2a78b5;
}
*{box-sizing:border-box;margin:0;padding:0}
html,body{width:1200px;height:4460px;overflow:hidden}
body{font-family:'Roboto',sans-serif;color:var(--ink);background:var(--white);position:relative}
.sec{position:absolute;left:0;width:1200px}
.fill{display:block}

/* header + hero */
.hero{top:0;height:640px;background:linear-gradient(90deg,#3c3c3a 0%,#4b4a46 55%,#6a625a 100%)}
.hero-photo{position:absolute;right:0;top:0;width:520px;height:640px;background:radial-gradient(circle at 70% 45%,#8a6d57 0%,#5a4a3e 40%,rgba(70,64,58,0) 75%)}
.logo{position:absolute;left:110px;top:0;width:200px;height:180px;background:var(--white);border-radius:0 0 90px 90px;display:flex;align-items:center;justify-content:center;gap:10px;z-index:3;box-shadow:0 4px 12px rgba(0,0,0,.25)}
.logo .dot{width:22px;height:22px;background:var(--ink);border-radius:50%}
.logo span{font-family:'Kanit',sans-serif;font-style:italic;font-weight:900;font-size:36px;color:var(--ink)}
.topbar{position:absolute;right:0;top:0;width:820px;height:40px;background:var(--red);display:flex;align-items:center;justify-content:space-between;padding:0 20px 0 60px;clip-path:polygon(30px 0,100% 0,100% 100%,0 100%)}
.search{width:300px;height:26px;background:var(--white);border-radius:3px;font-size:13px;color:#777;padding:5px 10px}
.social{display:flex;gap:10px}
.social i{width:20px;height:20px;border-radius:50%;background:var(--white);display:block}
.nav{position:absolute;right:0;top:56px;width:860px;height:56px;background:var(--white);display:flex;align-items:center;gap:46px;padding-left:100px;font-weight:700;font-size:15px;clip-path:polygon(30px 0,100% 0,100% 100%,0 100%)}
.nav a{color:var(--ink);text-decoration:none}
.nav a.active{color:var(--red);border-bottom:3px solid var(--red);padding-bottom:4px}
.hero h1{position:absolute;left:110px;top:270px;font-family:'Kanit',sans-serif;font-style:italic;font-weight:900;color:var(--white);text-transform:uppercase;line-height:.95;letter-spacing:2px}
.hero h1 .l1{font-size:64px;display:block}
.hero h1 .l2{font-size:110px;display:block}
.btn{display:inline-block;background:var(--red);color:var(--white);font-weight:700;font-size:14px;text-transform:uppercase;padding:16px 30px;transform:skewX(-12deg);box-shadow:6px 6px 0 rgba(0,0,0,.25)}
.btn span{display:inline-block;transform:skewX(12deg)}
.hero .btn{position:absolute;left:122px;top:440px}
.dots{position:absolute;left:570px;top:574px;display:flex;gap:10px}
.dots i{width:10px;height:10px;border-radius:50%;background:#999;display:block}
.dots i:first-child{background:var(--red)}

/* ad banner */
.ad-banner{top:700px;left:110px;width:980px;height:240px;background:linear-gradient(90deg,#f4d7c8 0%,#f8f3ee 45%,#fff 60%);border:1px solid var(--line);overflow:hidden}
.ad-banner .badge{position:absolute;left:355px;top:70px;width:110px;height:110px;border-radius:50%;background:var(--red);color:var(--white);font-weight:700;font-size:26px;display:flex;flex-direction:column;align-items:center;justify-content:center;line-height:1}
.ad-banner .badge small{font-size:18px}
.ad-copy{position:absolute;right:80px;top:24px;width:420px;text-align:center}
.ad-copy h3{font-family:'Roboto',sans-serif;font-weight:700;color:#1b8a3a;font-size:64px;line-height:1;text-transform:uppercase}
.ad-copy p{font-family:'Playfair Display',serif;font-style:italic;font-weight:800;color:var(--red);font-size:36px;line-height:1.2;margin-top:10px}
.ad-photo{position:absolute;left:0;top:0;width:340px;height:240px;background:linear-gradient(135deg,#e7a08d,#f3c9b6)}

.title{position:absolute;left:0;width:1200px;text-align:center;font-family:'Kanit',sans-serif;font-style:italic;font-weight:900;font-size:48px;line-height:1.1;text-transform:uppercase;letter-spacing:1px}
.title em{color:var(--red);font-style:italic}
.center-btn{position:absolute;left:0;width:1200px;text-align:center}

/* nutrition */
.nutri{top:960px;height:780px}
.nutri .title{top:50px}
.feature{position:absolute;left:110px;top:120px;width:630px;height:470px;background:linear-gradient(135deg,#d8cbbb,#eee5d8 50%,#c9b8a4)}
.feature-card{position:absolute;left:40px;bottom:20px;width:550px;background:var(--white);padding:16px 20px;text-align:center;box-shadow:0 2px 8px rgba(0,0,0,.15)}
.feature-card h4{font-family:'Playfair Display',serif;font-style:italic;font-weight:800;font-size:15px}
.feature-card .date{color:var(--red);font-size:11px;font-weight:700;margin:4px 0}
.feature-card p{font-size:11px;color:var(--text);line-height:1.4}
.side{position:absolute;left:780px;top:120px;width:310px}
.side-ad{height:170px;background:linear-gradient(135deg,#f6e7c8,#cfe6b7);position:relative;border:1px solid var(--line)}
.side-ad b{position:absolute;left:10px;top:14px;font-weight:700;font-size:20px;line-height:1.1;width:110px}
.mini{display:flex;gap:14px;margin-top:22px}
.mini .thumb{width:100px;height:80px;flex:none}
.mini p{font-size:11px;color:var(--text);line-height:1.35}
.mini .date{font-size:10px;color:#999;margin-top:5px}
.mini .more{font-size:11px;font-weight:700;margin-top:3px}
.nutri .center-btn{top:650px}

/* training */
.train{top:1740px;height:740px;background:var(--grey)}
.train .title{top:45px}
.cards{position:absolute;left:110px;top:130px;width:980px;display:flex;justify-content:space-between}
.tcard{width:295px;background:var(--white);box-shadow:0 3px 10px rgba(0,0,0,.15);border-bottom:4px solid var(--red);padding-bottom:20px;text-align:center}
.tcard.active{outline:5px solid var(--red)}
.tcard .thumb{height:185px}
.tcard h4{font-family:'Playfair Display',serif;font-style:italic;font-weight:800;font-size:17px;margin:18px 0 4px}
.tcard .date{color:var(--red);font-size:12px;font-weight:700}
.tcard p{font-size:14px;color:var(--text);line-height:1.5;padding:10px 24px 0}
.train .center-btn{top:600px}

/* workouts */
.work{top:2480px;height:650px}
.work .title{top:55px}
.wcards{position:absolute;left:110px;top:135px;display:flex;gap:22px}
.wcard{width:300px;text-align:center}
.wcard .thumb{height:265px}
.wcard .date{color:var(--red);font-size:14px;font-weight:700;margin-top:12px}
.wcard h4{font-family:'Playfair Display',serif;font-style:italic;font-weight:800;font-size:17px;line-height:1.3;margin-top:4px}
.follow{position:absolute;left:768px;top:135px;width:322px}
.follow h5{font-size:12px;font-weight:700;text-transform:uppercase;margin-bottom:8px}
.srow{height:44px;display:flex;align-items:center;color:var(--white);font-size:11px;font-weight:700;margin-bottom:9px;padding-left:10px;gap:10px}
.srow i{width:22px;height:22px;border-radius:50%;background:rgba(255,255,255,.85);display:block}
.srow .act{margin-left:auto;height:26px;width:60px;margin-right:8px;background:rgba(255,255,255,.25);display:flex;align-items:center;justify-content:center;border-radius:3px}
.fb{background:var(--fb)}.tw{background:var(--tw)}.ig{background:var(--ig)}.li{background:var(--in)}
.gym-ad{height:110px;background:linear-gradient(90deg,#2c2c2c,#111);position:relative;margin-top:8px}
.gym-ad b{position:absolute;right:14px;top:18px;color:var(--white);font-size:22px;text-align:right;line-height:1.1}
.gym-ad small{display:block;font-size:12px;font-weight:500;margin-top:6px}
.gym-ad .buy{position:absolute;right:14px;bottom:12px;background:var(--white);color:var(--ink);font-size:10px;font-weight:700;padding:4px 8px}
.work .center-btn{top:540px}

/* webinar */
.webinar{top:3140px;left:110px;width:980px;height:280px;background:#1a1a1a;overflow:hidden}
.web-photo{position:absolute;left:0;top:0;width:560px;height:280px;background:linear-gradient(90deg,#8e8a86,#5d5956 70%,#1a1a1a)}
.web-copy{position:absolute;right:30px;top:56px;text-align:right;color:var(--white)}
.web-copy .gym{font-size:16px;font-weight:700;letter-spacing:2px;display:flex;align-items:center;justify-content:flex-end;gap:8px}
.web-copy .gym i{width:14px;height:14px;border-radius:50%;background:var(--red);display:block}
.web-copy h3{font-family:'Kanit',sans-serif;font-style:italic;font-weight:900;font-size:52px;line-height:.95;text-transform:uppercase;margin-top:16px}
.web-copy h3 em{color:var(--red);display:block;font-style:italic}

/* forum */
.forum{top:3420px;height:740px;background:var(--grey)}
.forum .title{top:55px}
.frow{position:absolute;left:110px;width:980px;height:94px;background:var(--white);border:1px solid var(--line);display:flex;align-items:center;padding:0 30px 0 24px;gap:20px}
.avatar{width:48px;height:48px;border-radius:50%;background:#9aa2ad;flex:none}
.ftext h4{font-family:'Playfair Display',serif;font-style:italic;font-weight:800;font-size:15px}
.ftext p{font-size:11px;color:var(--text);margin-top:6px}
.ftext p b{color:var(--ink)}
.stats{margin-left:auto;font-size:11px;color:var(--text);line-height:1.8;display:flex;flex-direction:column}
.stats span::before{content:'';display:inline-block;width:8px;height:8px;background:var(--ink);border-radius:50%;margin-right:8px}

/* cta + footer */
.cta{top:4060px;left:110px;width:980px;height:130px;background:var(--red);color:var(--white);display:flex;align-items:center;padding:0 40px;gap:40px;z-index:2;box-shadow:0 6px 14px rgba(0,0,0,.25);border-radius:6px 0 6px 0}
.cta h3{font-family:'Playfair Display',serif;font-style:italic;font-weight:800;font-size:22px;line-height:1.2;width:330px}
.cta p{font-size:13px;line-height:1.45;width:380px}
.cta .out{margin-left:auto;background:var(--white);color:var(--red);font-weight:700;font-size:13px;padding:12px 26px;text-transform:uppercase;white-space:nowrap}
.footer{top:4160px;height:300px;background:#0b0b0b;color:var(--white)}
.flogo{position:absolute;left:120px;top:110px;display:flex;align-items:center;gap:10px}
.flogo .dot{width:20px;height:20px;border-radius:50%;background:var(--white)}
.flogo span{font-family:'Kanit',sans-serif;font-style:italic;font-weight:900;font-size:36px}
.fnav{position:absolute;left:450px;top:85px;display:flex;gap:54px;font-weight:700;font-size:14px}
.fcontact{position:absolute;left:450px;top:130px;display:flex;gap:120px;font-size:12px}
.fcontact span{display:flex;align-items:center;gap:8px}
.fcontact svg{fill:var(--red)}
.fcopyright{position:absolute;left:450px;top:172px;font-size:11px;color:#bbb}
.fsocial{position:absolute;left:450px;top:204px;display:flex;gap:12px}
.fsocial i{width:26px;height:26px;border-radius:50%;background:var(--red);display:block}
</style>
</head>
<body>

<section class="sec hero">
  <div class="hero-photo" role="img" aria-label="Muscular arm holding a black shaker bottle"></div>
  <div class="logo"><i class="dot"></i><span>GRIND</span></div>
  <div class="topbar">
    <div class="search">Search</div>
    <div class="social"><i></i><i></i><i></i><i></i></div>
  </div>
  <nav class="nav">
    <a class="active" href="#">Home</a><a href="#">Nutrition</a><a href="#">Training</a><a href="#">Workout</a><a href="#">Forum For Speaking</a><a href="#">Contact Us</a>
  </nav>
  <h1><span class="l1">Built on the</span><span class="l2">Grind</span></h1>
  <a class="btn"><span>Get Started</span></a>
  <div class="dots"><i></i><i></i><i></i></div>
</section>

<aside class="sec ad-banner">
  <div class="ad-photo" role="img" aria-label="Woman eating a fresh salad"></div>
  <div class="badge">50%<small>OFF</small></div>
  <div class="ad-copy"><h3>Fitness<br>Nutrition</h3><p>Eating healthy now!</p></div>
</aside>

<section class="sec nutri">
  <h2 class="title">Our <em>Nutrition</em></h2>
  <article class="feature" role="img" aria-label="Two women preparing healthy food in a kitchen">
    <div class="feature-card">
      <h4>Blanditiis Praesentium Voluptatum Deleniti</h4>
      <div class="date">June 17, 2022</div>
      <p>Eaque earum rerum hic tenetur a sapiente delectus, ut aut reiciendis voluptatibus maiores alias consequatur aut perferendis doloribus asperiores repellat.</p>
    </div>
  </article>
  <div class="side">
    <div class="side-ad" role="img" aria-label="Dessert giveaway advert with fruit bowl"><b>WIN A FREE DESSERT!</b></div>
    <div class="mini"><div class="thumb fill" style="background:linear-gradient(135deg,#e9b35a,#c97a3a)" role="img" aria-label="Woman drinking a smoothie"></div><div><p>Eaque earum rerum hic tenetur a sapiente delectus, ut reiciendis voluptatibus.</p><div class="date">January 20, 2022</div><div class="more">Read More</div></div></div>
    <div class="mini"><div class="thumb fill" style="background:linear-gradient(135deg,#c98a6a,#7c5a4a)" role="img" aria-label="Man eating a healthy meal"></div><div><p>Eaque earum rerum hic tenetur a sapiente delectus, ut reiciendis voluptatibus.</p><div class="date">January 20, 2022</div><div class="more">Read More</div></div></div>
    <div class="mini"><div class="thumb fill" style="background:linear-gradient(135deg,#8fb35a,#d9a24a)" role="img" aria-label="Bowl of fruit and vegetables"></div><div><p>Eaque earum rerum hic tenetur a sapiente delectus, ut reiciendis voluptatibus.</p><div class="date">January 20, 2022</div><div class="more">Read More</div></div></div>
  </div>
  <div class="center-btn"><a class="btn"><span>Learn More</span></a></div>
</section>

<section class="sec train">
  <h2 class="title">Our <em>Training</em></h2>
  <div class="cards">
    <article class="tcard"><div class="thumb fill" style="background:linear-gradient(135deg,#555,#9a8f86)" role="img" aria-label="Group doing push-ups in a gym"></div><h4>Finibus Bonorum</h4><div class="date">Feb 04, 2023</div><p>Quis autem vel eum iure reprehenderit qui in ea voluptate velit esse quam nihil molestiae consequatur, quo voluptas nulla pariatur.</p></article>
    <article class="tcard active"><div class="thumb fill" style="background:linear-gradient(135deg,#7a2a2a,#c35a4a)" role="img" aria-label="Indoor cycling class"></div><h4>Voluptu Accusanti</h4><div class="date">Mar 24, 2023</div><p>Excepteur sint occaecat cupidatat non proident, sunt in culpa qui officia mollit exercitation ullamco laboris nisi ut aliquip ex laborum.</p></article>
    <article class="tcard"><div class="thumb fill" style="background:linear-gradient(135deg,#3a3a40,#7f7a80)" role="img" aria-label="Woman training on a spin bike"></div><h4>Tempor Incididunt</h4><div class="date">Nov 11, 2022</div><p>Quis autem vel eum iure reprehenderit qui in ea voluptate velit esse quam nihil molestiae consequatur, quo voluptas nulla pariatur.</p></article>
  </div>
  <div class="center-btn"><a class="btn"><span>View More</span></a></div>
</section>

<section class="sec work">
  <h2 class="title">Our <em>Workouts</em></h2>
  <div class="wcards">
    <article class="wcard"><div class="thumb fill" style="background:linear-gradient(135deg,#2f8fa8,#6a6a6a)" role="img" aria-label="Two people doing plank exercises"></div><div class="date">October 18, 2022</div><h4>Finibus Bonorum et<br>Blanditiis</h4></article>
    <article class="wcard"><div class="thumb fill" style="background:linear-gradient(135deg,#5a5a5a,#a9a39c)" role="img" aria-label="Gym with people training on machines"></div><div class="date">June 23, 2022</div><h4>Excepteur sint occaecat cupid atat non proident</h4></article>
  </div>
  <aside class="follow">
    <h5>Subscribe &amp; Follow</h5>
    <div class="srow fb"><i></i>12,456 Likes<span class="act">Like</span></div>
    <div class="srow tw"><i></i>256 Followers<span class="act">Follow</span></div>
    <div class="srow ig"><i></i>784 Followers<span class="act">Follow</span></div>
    <div class="srow li"><i></i>356 Followers<span class="act">Follow</span></div>
    <div class="gym-ad" role="img" aria-label="Gym advert with a bodybuilder"><b>Get 20% Off<small>Gym membership deal</small></b><span class="buy">JOIN NOW</span></div>
  </aside>
  <div class="center-btn"><a class="btn"><span>See More</span></a></div>
</section>

<aside class="sec webinar">
  <div class="web-photo" role="img" aria-label="Woman lifting a barbell"></div>
  <div class="web-copy">
    <div class="gym"><i></i>GYM<br>NAME</div>
    <h3>Personal<em>Training</em>Webinar</h3>
  </div>
</aside>

<section class="sec forum">
  <h2 class="title">Forum for <em>Speaking</em></h2>
  <div class="frow" style="top:140px"><i class="avatar"></i><div class="ftext"><h4>Quis autem vel eum iure reprehenderit</h4><p><b>Accusantium doloremque</b> occaecat cupidatat &nbsp;&nbsp;&nbsp; <b>Accusantium doloremque</b> occaecat cupidatat</p></div><div class="stats"><span>45</span><span>78</span></div></div>
  <div class="frow" style="top:254px"><i class="avatar"></i><div class="ftext"><h4>Itaque earum rerum hic tenetur a sapiente delectus, ut aliquitibus</h4><p><b>Accusantium doloremque</b> occaecat cupidatat &nbsp;&nbsp;&nbsp; <b>Accusantium doloremque</b> occaecat cupidatat</p></div><div class="stats"><span>45</span><span>78</span></div></div>
  <div class="frow" style="top:368px"><i class="avatar"></i><div class="ftext"><h4>Quis autem vel eum iure reprehenderit</h4><p><b>Accusantium doloremque</b> occaecat cupidatat &nbsp;&nbsp;&nbsp; <b>Accusantium doloremque</b> occaecat cupidatat</p></div><div class="stats"><span>45</span><span>78</span></div></div>
  <div class="frow" style="top:482px"><i class="avatar"></i><div class="ftext"><h4>Itaque earum rerum hic tenetur a sapiente delectus, ut aliquitibus</h4><p><b>Accusantium doloremque</b> occaecat cupidatat &nbsp;&nbsp;&nbsp; <b>Accusantium doloremque</b> occaecat cupidatat</p></div><div class="stats"><span>45</span><span>78</span></div></div>
</section>

<aside class="sec cta">
  <h3>Temporibus autem quibusdam et aut officiis</h3>
  <p>Eaque earum rerum hic tenetur a sapiente delectus, ut aut reiciendis voluptatibus maiores alias consequatur aut perferendis doloribus asperiores repellat.</p>
  <span class="out">Get More</span>
</aside>

<footer class="sec footer">
  <div class="flogo"><i class="dot"></i><span>GRIND</span></div>
  <nav class="fnav"><span>Home</span><span>Nutrition</span><span>Training</span><span>Workouts</span><span>Forums</span><span>Contact Us</span></nav>
  <div class="fcontact">
    <span><svg width="14" height="14" viewBox="0 0 24 24"><path d="M6.6 10.8a15 15 0 0 0 6.6 6.6l2.2-2.2a1 1 0 0 1 1-.25 11.4 11.4 0 0 0 3.6.57 1 1 0 0 1 1 1V20a1 1 0 0 1-1 1A17 17 0 0 1 3 4a1 1 0 0 1 1-1h3.5a1 1 0 0 1 1 1c0 1.25.2 2.45.57 3.57a1 1 0 0 1-.25 1z"/></svg>Phone: +1 555 010 2040</span>
    <span><svg width="14" height="14" viewBox="0 0 24 24"><path d="M2 5h20v14H2zm2 2v.5l8 5 8-5V7l-8 5z"/></svg>Email: hello@grindfitness.example</span>
  </div>
  <div class="fcopyright">Copyright 2023 Grind Fitness Co. All Rights Reserved</div>
  <div class="fsocial"><i></i><i></i><i></i><i></i></div>
</footer>

</body>
</html>
```